Store Promo Card (already have logo!)

I need a card design (single side) for my online women’s gift shop containing a promotional code to be placed in bags for attendees at an event. I’m flexible on both shape and sizing, but perhaps a 4x6 card.
—It should contain my attached logo, my website (www.merrowlyn.com), and my Instagram handle (@merrowlyn) and promotion language such as “15% off your purchase with code: PIVRAL”.
—I think I would like my logo to be large.
—It should be clean, simple and modern in design and should use the colors from my logo.
—I would like about 3-5 product pictures depending on design.
Target Market(s)
Women ages 30 to 60
Industry/Entity Type
Retail Upscale Gift

```html
<!DOCTYPE html>
<html lang="en">
<head>
<meta charset="utf-8">
<title>Merrowlyn Promo Card</title>
<link rel="stylesheet" href="https://fonts.googleapis.com/css2?family=Abril+Fatface&display=swap">
<style>
  :root {
    --rose-gold-light: #f0d2c2;
    --rose-gold: #d8a592;
    --rose-gold-deep: #b98574;
    --spot-brown: #5b4a41;
    --petal-white: #f6eeea;
    --petal-pink: #e89a9a;
    --petal-deep: #d9707a;
    --ink-white: #f7efec;
    --frame-white: #f1e4df;
    --shadow: rgba(60, 35, 28, 0.55);
  }
  * { margin: 0; padding: 0; box-sizing: border-box; }
  html, body {
    width: 1200px;
    height: 800px;
    overflow: hidden;
    background: #ffffff;
  }
  .promo-card {
    position: relative;
    width: 1200px;
    height: 800px;
    overflow: hidden;
    font-family: "Abril Fatface", "Bodoni Moda", serif;
    color: var(--ink-white);
  }
  .pattern-field {
    position: absolute;
    inset: 0;
    background:
      radial-gradient(ellipse at 30% 45%, rgba(240, 210, 194, 0.85) 0%, rgba(240, 210, 194, 0) 55%),
      linear-gradient(135deg, var(--rose-gold) 0%, #c8998a 45%, #a98274 100%);
  }
  .rose-art {
    position: absolute;
    inset: 0;
    width: 1200px;
    height: 800px;
  }
  .frame-box {
    position: absolute;
    left: 65px;
    top: 200px;
    width: 1072px;
    height: 374px;
    border: 5px solid var(--frame-white);
    box-shadow: 2px 3px 4px var(--shadow), inset 2px 3px 4px rgba(60, 35, 28, 0.25);
    background: linear-gradient(100deg, rgba(225, 170, 150, 0.55) 0%, rgba(245, 215, 198, 0.55) 45%, rgba(205, 150, 132, 0.35) 100%);
  }
  .offer-headline {
    position: absolute;
    left: 0;
    width: 1200px;
    top: 22px;
    text-align: center;
    font-size: 152px;
    line-height: 1;
    letter-spacing: 2px;
    color: var(--ink-white);
    text-shadow: 2px 3px 4px var(--shadow);
  }
  .brand-name {
    position: absolute;
    left: 65px;
    width: 1072px;
    top: 300px;
    text-align: center;
    font-size: 124px;
    line-height: 1;
    letter-spacing: 1px;
    color: var(--ink-white);
  }
  .promo-line {
    position: absolute;
    left: 0;
    width: 1200px;
    top: 648px;
    text-align: center;
    font-size: 35px;
    line-height: 1;
    letter-spacing: 0.5px;
    color: var(--ink-white);
    text-shadow: 2px 2px 3px var(--shadow);
  }
  .contact-row {
    position: absolute;
    top: 738px;
    font-size: 33px;
    line-height: 1;
    color: var(--ink-white);
    text-shadow: 2px 2px 3px var(--shadow);
  }
  .contact-web { left: 113px; }
  .contact-social {
    left: 773px;
    display: flex;
    align-items: center;
    gap: 10px;
  }
  .social-marker {
    width: 28px;
    height: 28px;
    border-radius: 7px;
    background: var(--petal-deep);
  }
</style>
</head>
<body>
<main class="promo-card">
  <div class="pattern-field" role="img" aria-label="Rose gold background with a brown leopard print pattern"></div>

  <svg class="rose-art" viewBox="0 0 1200 800" aria-hidden="true">
    <defs>
      <radialGradient id="rose-large-fill" cx="0.45" cy="0.45" r="0.6">
        <stop offset="0" stop-color="#e27d84"/>
        <stop offset="0.45" stop-color="#eeb1ae"/>
        <stop offset="1" stop-color="#f6eeea"/>
      </radialGradient>
      <radialGradient id="rose-small-fill" cx="0.35" cy="0.4" r="0.65">
        <stop offset="0" stop-color="#ec9ea0"/>
        <stop offset="0.5" stop-color="#f4cfcc"/>
        <stop offset="1" stop-color="#f8f0ee"/>
      </radialGradient>
    </defs>
    <g role="img" aria-label="Large pale pink rose bloom">
      <path d="M455 40 C470 -10 560 -20 640 0 L1200 0 L1200 520 C1160 540 1120 520 1090 560 C1060 600 1000 620 930 610 C860 600 800 620 740 590 C680 560 640 500 610 450 C560 400 500 360 500 290 C500 220 470 160 480 110 C485 80 450 70 455 40 Z" fill="url(#rose-large-fill)"/>
    </g>
    <g role="img" aria-label="Small pink rose in the lower left corner">
      <path d="M0 478 C60 470 110 500 130 540 C170 580 220 620 240 680 C255 730 240 780 225 800 L0 800 Z" fill="url(#rose-small-fill)"/>
    </g>
  </svg>

  <div class="frame-box"></div>

  <h1 class="offer-headline">15% OFF</h1>

  <p class="brand-name">MERROWLYN</p>

  <p class="promo-line">YOUR PURCHASE WITH CODE: PIVRAL</p>

  <p class="contact-row contact-web">WWW.MERROWLYN.COM</p>
  <p class="contact-row contact-social"><span class="social-marker"></span>@MERROWLYN</p>
</main>
</body>
</html>
```